Postcard Mailer to upscale luxury homeowners

We are a new company in the Tucson AZ market and want to use postcard marketing in key target markets. We clean and seal natural stone - granite, travertine, slate, etc. See website - http://www.brightvaultcoatings.example/ for more information about about our services and before/after photos in our "gallery" section.The logo from the site - Bright Vault Coatings - needs to be on the post card. The before/after photos from the photo "gallery" on the site demonstrate what can be done. We think a promo of $XXX off to any one requesting an estimate and presenting the postcard is worth trying. We have additional photos and information if needed.

Target Market(s)

Upscale residential homes in luxury home subdivisions

Industry/Entity Type

Home Improvement

Font styles to use
Sans Serif
Script

Requirements
Must have
• Logo
• Before/After photo (see website gallery for potential photos)
• website
• contact
• life time guarantee
• Feel of richness
Nice to have
• A call to action. $XXX dollar discount when estimate scheduled within/by ZZ
Should not have
• Won't know until I see it

```html
<!DOCTYPE html>
<html lang="en">
<head>
<meta charset="utf-8">
<title>Bright Vault Coatings Postcard</title>
<link rel="stylesheet" href="https://fonts.googleapis.com/css2?family=Oswald:wght@500;600&family=Crimson+Text:ital,wght@0,400;0,700;1,400&family=Arimo&display=swap">
<style>
:root{
  --panel-blue:#4a8cb7;
  --navy:#1f5585;
  --ink:#1d1d1d;
  --link-blue:#2f78b0;
  --white:#ffffff;
  --sky-top:#cfe2ee;
  --sky-bottom:#f7fbfd;
  --line-grey:#8b9096;
}
*{margin:0;padding:0;box-sizing:border-box}
html,body{width:932px;height:1200px;overflow:hidden;background:var(--white)}
.canvas{position:relative;width:932px;height:1200px}
.card{position:absolute;left:34px;width:898px;overflow:hidden}
.card-front{top:30px;height:580px}
.card-back{top:628px;height:570px;background:linear-gradient(180deg,var(--sky-top) 0%,var(--sky-bottom) 45%,var(--sky-top) 100%)}

.kitchen-photo{position:absolute;inset:0;background:linear-gradient(135deg,#7a5a3e 0%,#c9a27a 30%,#e8d2b0 45%,#8a5a33 65%,#2a2220 100%)}
.blue-panel{position:absolute;inset:0}
.tv-badge{position:absolute;left:36px;top:490px;width:157px;height:67px;background:#e7d23a;border:2px solid #c5b020}

.front-copy{position:absolute;right:30px;color:var(--white);text-align:right}
.headline{top:40px;font-family:'Oswald',sans-serif;font-weight:600;font-size:23px;line-height:30px}
.tagline{top:100px;font-family:'Crimson Text',serif;font-style:italic;font-size:22px;line-height:24px}
.call-line{top:413px;font-family:'Crimson Text',serif;font-style:italic;font-size:22px;line-height:26px;right:22px}
.front-phone{top:474px;font-family:'Oswald',sans-serif;font-weight:600;font-size:36px;right:22px;letter-spacing:.5px}
.front-web{top:524px;font-family:'Oswald',sans-serif;font-weight:600;font-size:25px;right:22px}

.brand-seal{position:absolute;border-radius:50%;background:var(--white);border:6px solid var(--navy);display:flex;align-items:center;justify-content:center;text-align:center;font-family:'Oswald',sans-serif;font-weight:600;color:var(--navy);text-transform:uppercase}
.brand-seal-front{left:650px;top:175px;width:228px;height:228px;font-size:27px;line-height:34px}
.brand-seal-back{left:24px;top:399px;width:136px;height:136px;font-size:16px;line-height:20px;border-width:4px}

.result-photo{position:absolute;top:35px;width:202px;height:150px;border:3px solid var(--navy)}
.result-before{left:32px;background:linear-gradient(135deg,#8b6a55,#b48a70 40%,#6e5547 70%,#a08070)}
.result-after{left:239px;background:linear-gradient(135deg,#7a4a38,#b8765a 40%,#6a3f30 70%,#c08a70)}
.result-tag{position:absolute;left:4px;top:4px;background:var(--white);color:var(--navy);font-family:'Crimson Text',serif;font-weight:700;font-size:15px;padding:1px 6px}

.about{position:absolute;left:27px;top:216px;width:226px;font-family:'Crimson Text',serif;font-size:15.5px;line-height:19.5px;color:var(--ink)}
.about strong{font-weight:700}
.about .services{color:var(--link-blue)}
.reasons{position:absolute;left:278px;top:216px;width:190px;font-family:'Crimson Text',serif;font-size:15.5px;line-height:20.5px;color:var(--ink)}
.reasons h2{font-weight:400;font-size:15.5px;color:var(--link-blue);margin-bottom:1px}
.reasons ul{padding-left:26px}
.cta{position:absolute;left:170px;top:415px;font-family:'Crimson Text',serif;color:var(--navy)}
.cta p{font-size:26px;line-height:32px}
.cta .back-phone{font-weight:700;font-size:26px;margin-top:12px}

.return-address{position:absolute;left:542px;top:34px;font-family:'Arimo',sans-serif;font-size:11.5px;line-height:18px;color:var(--ink);letter-spacing:-.2px}
.postmark{position:absolute;left:730px;top:24px}
.mailing-lines{position:absolute;left:537px;top:270px;width:338px}
.mailing-lines span{display:block;border-top:1.5px dashed var(--line-grey);height:60px}
</style>
</head>
<body>
<div class="canvas">

  <section class="card card-front">
    <div class="kitchen-photo" role="img" aria-label="Luxury kitchen with stone arch hood, granite island and pendant lights"></div>
    <svg class="blue-panel" width="898" height="580" viewBox="0 0 898 580" aria-hidden="true">
      <path d="M520 0 L898 0 L898 580 L515 580 C580 520 640 450 640 360 C640 250 620 150 600 100 C585 60 560 25 520 0 Z" fill="var(--panel-blue)"/>
      <path d="M520 0 C560 25 585 60 600 100 C620 150 640 250 640 360 C640 450 580 520 515 580" fill="none" stroke="#ffffff" stroke-width="3" opacity=".7"/>
    </svg>
    <div class="tv-badge" role="img" aria-label="As seen on TV badge"></div>
    <p class="front-copy headline">Quality Granite &amp; Natural<br>Stone Sealing &amp; Cleaning</p>
    <p class="front-copy tagline">Top quality services and<br>competitive pricing!</p>
    <div class="brand-seal brand-seal-front">Bright Vault<br>Coatings</div>
    <p class="front-copy call-line">Give us a call today<br>for a free estimate!</p>
    <p class="front-copy front-phone">520.555.0147</p>
    <p class="front-copy front-web">www.brightvaultcoatings.example</p>
  </section>

  <section class="card card-back">
    <div class="result-photo result-before" role="img" aria-label="Dull, stained slate tile floor before cleaning"><span class="result-tag">BEFORE</span></div>
    <div class="result-photo result-after" role="img" aria-label="Glossy, restored slate tile floor after sealing"><span class="result-tag">AFTER</span></div>

    <p class="about">We are a small, <strong>family-owned business</strong>, so you can have full confidence that you will receive <strong>friendly, personalized service</strong> when you work with us! We offer <span class="services">stone cleaning and sealing, surface restoration, tile or grout services, and more.</span></p>

    <div class="reasons">
      <h2>WHY CHOOSE US</h2>
      <ul>
        <li>As Seen on Casa Living TV</li>
        <li>Trade Guild Accredited</li>
        <li>Family Owned and Operated</li>
        <li>One Time Process!</li>
        <li>Lifetime Warranty Against Staining</li>
      </ul>
    </div>

    <div class="brand-seal brand-seal-back">Bright Vault<br>Coatings</div>
    <div class="cta">
      <p>Request a free estimate,<br>give us a call today!</p>
      <p class="back-phone">520.555.0147</p>
    </div>

    <p class="return-address">1180 W Canyon Mesa Rd<br>Suite 210<br>Tucson, AZ 85705</p>
    <svg class="postmark" width="150" height="90" viewBox="0 0 150 90" aria-hidden="true">
      <circle cx="105" cy="40" r="38" fill="none" stroke="#8e959b" stroke-width="1.5"/>
      <circle cx="105" cy="40" r="31" fill="none" stroke="#8e959b" stroke-width="1.5"/>
      <g fill="none" stroke="#6f767c" stroke-width="2.5">
        <path d="M2 30 q10 -8 20 0 t20 0 t20 0 t20 0 t20 0"/>
        <path d="M2 42 q10 -8 20 0 t20 0 t20 0 t20 0 t20 0"/>
        <path d="M2 54 q10 -8 20 0 t20 0 t20 0 t20 0 t20 0"/>
        <path d="M2 66 q10 -8 20 0 t20 0 t20 0 t20 0"/>
      </g>
    </svg>
    <div class="mailing-lines"><span></span><span></span><span></span></div>
  </section>

</div>
</body>
</html>
```